Window Graphics for Chiropractic office

I need graphics design for my storefront windows for my chiropractic office. The city is very strict about how much of the windows can be covered. They don't allow for perforated decals at all. I will upload the specifics. The lettering and any graphics cannot occupy more than 20% of the windows. The lettering cannot be higher than 6 inches tall. The design that is need here will be submitted to a graphics design department where they design it on their software at the printing company. So it doesn't really matter here how clear the pics are etc. The design proofs I received from the printing company were very disappointing which is the reason I am requesting some designs from here. The door already has graphics on it that should match what is being designed on the window panes.
My office is spa, beachy like inside. I wouldn't mind something that exudes relaxation. I treat a lot of pregnant women and families as well as auto injuries.
Per the city, they state , "Window signs shall not exceed an aggregate area equal to 20 percent of the window on which they are located, or 9 square feet per window, whichever is less. Letter heights on window signs shall be a maximum of 6 inches."
Enclosed is the proof the printing company provided which I think is very blah. Maybe some color and small banners?
The left pane should read
Prenatal Chiropractic Care
Low Back Pain
Musculoskeletal Pelvic Pain
Sciatic Pain
Hip Pain
Children & Families
Wellness care
Sports injuries
Scoliosis
Musculoskeletal Pain
The middle Pane can be left as is in terms of what it says, except it should say call or text us at 555-208-7931
The right pane should say
Auto Injuries
Whiplash
Low Back Pain & Sciatica
Carpal Tunnel Syndrome
Plantar Fascitis/Achilles Tendinitis
Knee/Shoulder Pain
I'd like some feminine akin to what is attached with the Prenatal attachm,ent. The writing there might be too hard to read far away, but I like the gist of it. If it doesn't match the door that is no big deal. I can chage it if I really like the window pane design.

```html
<!DOCTYPE html>
<html lang="en">
<head>
<meta charset="utf-8">
<title>Harbor Chiropractic – Storefront Window Graphics</title>
<link rel="stylesheet" href="https://fonts.googleapis.com/css2?family=Marcellus&family=Yellowtail&display=swap">
<style>
  :root {
    --wall: #dfc398;
    --floor: #7a6060;
    --frame: #5a5a5a;
    --glass: #383a40;
    --ink: #ffffff;
    --orange: #f7822f;
    --blue: #3f3fe4;
    --bone: #ffffff;
  }
  * { margin: 0; padding: 0; box-sizing: border-box; }
  html, body { width: 1200px; height: 757px; overflow: hidden; background: var(--wall); }
  .storefront { position: relative; width: 1200px; height: 757px; background: var(--wall); }
  .floor { position: absolute; left: 0; top: 679px; width: 1200px; height: 78px; background: var(--floor); }
  .frame { position: absolute; left: 59px; top: 46px; width: 1080px; height: 633px; background: var(--frame); }
  .pane { position: absolute; background: var(--glass); overflow: hidden; }
  .pane--left { left: 72px; top: 64px; width: 276px; height: 601px; }
  .pane--middle { left: 362px; top: 64px; width: 275px; height: 601px; }
  .pane--right { left: 654px; top: 64px; width: 275px; height: 601px; }
  .pane--transom { left: 944px; top: 64px; width: 184px; height: 164px; }
  .door { position: absolute; left: 944px; top: 239px; width: 184px; height: 439px; background: var(--frame); border: 1px solid #3a3a3a; }
  .pane--door { left: 16px; top: 18px; width: 151px; height: 394px; }
  .mullion { position: absolute; left: 59px; top: 488px; width: 870px; height: 17px; background: var(--frame); }

  .spine-band {
    position: absolute; left: 72px; top: 438px; width: 857px; height: 142px;
    background: linear-gradient(180deg, rgba(255,255,255,0.85), rgba(255,255,255,0.95) 50%, rgba(255,255,255,0.8));
    border-radius: 40px 0 0 8px;
  }
  .art-prenatal {
    position: absolute; left: 0; top: 103px; width: 108px; height: 321px;
    background: linear-gradient(180deg, var(--blue) 0%, var(--blue) 35%, var(--orange) 55%, var(--orange) 100%);
    border-radius: 50px 60px 0 0;
  }
  .art-emblem {
    position: absolute;
    background: linear-gradient(135deg, var(--orange) 0%, var(--blue) 55%, var(--orange) 100%);
  }
  .art-emblem--right { left: 118px; top: 71px; width: 220px; height: 460px; border-radius: 200px 0 0 200px; }
  .art-emblem--transom { left: 0; top: 71px; width: 184px; height: 120px; border-radius: 0 120px 0 0; }
  .art-emblem--door { left: 0; top: 0; width: 151px; height: 259px; border-radius: 0 0 140px 0; }

  .service-list {
    position: absolute; list-style: none; color: var(--ink);
    font-family: "Yellowtail", cursive; font-size: 21px; line-height: 24.4px;
  }
  .service-list--left { right: 10px; top: 11px; text-align: right; }
  .service-list--left .gap { height: 24.4px; }
  .service-list--right { left: 13px; top: 11px; }

  .practice { position: absolute; left: 0; top: 0; width: 275px; text-align: center; color: var(--ink); font-family: "Marcellus", serif; }
  .practice__mark { position: absolute; left: 120px; top: 60px; width: 36px; height: 36px; border: 2px solid var(--orange); border-radius: 50%; }
  .practice__name { position: absolute; left: 0; top: 164px; width: 275px; font-size: 18.5px; letter-spacing: 0.3px; }
  .practice__doctor { position: absolute; left: 0; top: 206px; width: 275px; font-size: 17px; line-height: 21px; }
  .practice__cta { position: absolute; left: 0; top: 270px; width: 275px; font-size: 17px; }
  .practice__phone { position: absolute; left: 0; top: 287px; width: 275px; font-size: 37px; letter-spacing: -0.5px; }

  .web { position: absolute; left: 0; top: 519px; width: 100%; text-align: center; color: var(--orange); font-family: "Marcellus", serif; font-size: 17.5px; }
  .pane--left .web { text-align: right; padding-right: 10px; }
</style>
</head>
<body>
<div class="storefront">
  <div class="floor"></div>
  <div class="frame"></div>

  <section class="pane pane--left">
    <div class="art-prenatal" role="img" aria-label="Line illustration of an expecting mother in orange and blue"></div>
    <ul class="service-list service-list--left">
      <li>Prenatal Chiropractic Care</li>
      <li>Low Back Pain</li>
      <li>Musculoskeletal Pelvic Pain</li>
      <li>Sciatic Pain</li>
      <li>Hip Pain</li>
      <li class="gap" aria-hidden="true"></li>
      <li>Children &amp; Families</li>
      <li>Wellness care</li>
      <li>Sports injuries</li>
      <li>Scoliosis</li>
      <li>Musculoskeletal Pain</li>
    </ul>
    <p class="web">HARBORCHIROPRACTIC.com</p>
  </section>

  <section class="pane pane--middle">
    <div class="practice">
      <span class="practice__mark" aria-hidden="true"></span>
      <h1 class="practice__name" style="font-weight:400">HARBOR CHIROPRACTIC</h1>
      <p class="practice__doctor">Dr. Maren Ellison, D.C.<br>Chiropractic Physician</p>
      <p class="practice__cta">call or text us at</p>
      <p class="practice__phone">555-208-7931</p>
    </div>
    <p class="web">HARBORCHIROPRACTIC.com</p>
  </section>

  <section class="pane pane--right">
    <div class="art-emblem art-emblem--right" role="img" aria-label="Large decorative emblem in orange and blue matching the door graphic"></div>
    <ul class="service-list service-list--right">
      <li>Auto Injuries</li>
      <li>Whiplash</li>
      <li>Low Back Pain &amp; Sciatica</li>
      <li>Carpal Tunnel Syndrome</li>
      <li>Plantar Fascitis/</li>
      <li>Achilles Tendinitis</li>
      <li>Knee/</li>
      <li>Shoulder Pain</li>
    </ul>
    <p class="web">HARBORCHIROPRACTIC.com</p>
  </section>

  <div class="pane pane--transom">
    <div class="art-emblem art-emblem--transom" aria-hidden="true"></div>
  </div>

  <div class="door">
    <div class="pane pane--door">
      <div class="art-emblem art-emblem--door" aria-hidden="true"></div>
    </div>
  </div>

  <div class="spine-band" role="img" aria-label="White illustrated spine running across the three window panes"></div>
  <div class="mullion"></div>
</div>
</body>
</html>
```